Business Card Design Project - KLB

I am looking for a more sophisticated card design for my company,
"The Lumen Collective"

We are a consultancy focused on strategy and change in Associations and professional organisations.

I am a lawyer and psychologist with a PhD and so am looking for something that communicates seriousness and credibility but also quirky creative solutions for strategic problems, which is my field of speciality.

I am looking for something that is quietly spoken, rather than loud colours ('credible' and 'creative' are the two adjectives that I think of as competing here).

I particularly like an embossed card style - heavy white card with plain white or white and black or white and grey text.

The key logo image for the company is a question mark and I am open to suggestions and ideas on design.

I have attached a file that includes a couple of styles that have caught my eye and my thoughts on them. Hopefully they communicate what I'm looking for.
Updates

Thank you for all the great suggestions and designs.

I really appreciated the effort and creative energy you put into your designs. I have now closed the project after selecting a design and advising the successful designer of the card that I am happy with.

Regards

Target Market(s)

Organisations (CEO's and Boards), Governments, Legal professionals, Membership Associations and aspiring professionals.

Industry/Entity Type

Lawyer

Requirements
Must have
• The key logo element is a question mark (?) and this needs to be incorporated.

Embossed style - cut outs or other design ideas interest me too.

The attached file has a number of sample ideas and comments on each one that I like.
Should not have
• I like crisp, modern fonts (Myriads etc...) and do not like embellished fonts or Times etc...

Files

```html
<!DOCTYPE html>
<html lang="en">
<head>
<meta charset="utf-8">
<title>The Lumen Collective — Business Card</title>
<link rel="stylesheet" href="https://fonts.googleapis.com/css2?family=Mulish:wght@600;700&family=Questrial&display=swap">
<style>
  :root {
    --backdrop: #dcd7d2;
    --card: #6b6c6e;
    --ink: #444547;
    --ink-soft: #4a4b4d;
    --mark: #ffffff;
  }
  * { margin: 0; padding: 0; box-sizing: border-box; }
  html, body { width: 1200px; height: 900px; overflow: hidden; }
  body {
    background: var(--backdrop);
    position: relative;
    font-family: "Questrial", "Century Gothic", sans-serif;
    color: var(--ink);
  }
  .card {
    position: absolute;
    top: 180px;
    width: 307px;
    height: 538px;
    background: var(--card);
    text-align: center;
  }
  .card--front { left: 267px; }
  .card--back  { left: 626px; }

  .brand-dot {
    position: absolute;
    left: 50%;
    transform: translateX(-50%);
    border-radius: 50%;
    background: var(--mark);
  }
  .card--front .brand-dot { top: 100px; width: 128px; height: 128px; }
  .card--back  .brand-dot { top: 50px;  width: 104px; height: 104px; }

  .brand-name {
    position: absolute;
    left: 0; right: 0;
    font-family: "Mulish", "Century Gothic", sans-serif;
    font-weight: 600;
    color: var(--ink);
  }
  .card--front .brand-name { top: 300px; font-size: 27px; line-height: 36px; }
  .card--back  .brand-name { top: 190px; font-size: 24px; line-height: 32px; }

  .website {
    position: absolute;
    left: 0; right: 0;
    top: 500px;
    font-size: 15px;
    color: var(--ink-soft);
  }

  .person {
    position: absolute;
    left: 0; right: 0;
    top: 296px;
    font-family: "Mulish", "Century Gothic", sans-serif;
    font-weight: 700;
    font-size: 15px;
    line-height: 20px;
  }
  .address {
    position: absolute;
    left: 0; right: 0;
    top: 358px;
    font-size: 15px;
    line-height: 20.5px;
    font-style: normal;
    color: var(--ink-soft);
  }
  .contact {
    position: absolute;
    left: 0; right: 0;
    top: 440px;
    font-size: 15px;
    line-height: 20.5px;
    color: var(--ink-soft);
    list-style: none;
  }
  .contact-label {
    font-family: "Mulish", "Century Gothic", sans-serif;
    font-weight: 700;
    color: var(--ink);
    margin-right: 8px;
  }
</style>
</head>
<body>
  <section class="card card--front" aria-label="Card front">
    <span class="brand-dot" aria-hidden="true"></span>
    <h1 class="brand-name">Lumen<br>Collective</h1>
    <p class="website">www.lumencollective.com.au</p>
  </section>

  <section class="card card--back" aria-label="Card back">
    <span class="brand-dot" aria-hidden="true"></span>
    <h2 class="brand-name">Lumen Collective</h2>
    <p class="person">Dr. Mara Ellison<br>Director</p>
    <address class="address">The Lumen Collective<br>P.O. Box 4180, Linden Grove,<br>Sydney, Australia</address>
    <ul class="contact">
      <li><span class="contact-label">M</span>+61400 000 214</li>
      <li><span class="contact-label">P</span>+612 9000 4471</li>
      <li><span class="contact-label">E</span>mara@lumencollective.com.au</li>
    </ul>
  </section>
</body>
</html>
```